Resposive web site in 4 languages + image gallery + logo design

We need a web page, which will work on all devices.
I have uploaded web page concept.
Company name: Quarnela
Industry/Entity Type
It Company
Logo Text
quality matters
Coding
Coded - Design and coding required
Number of Pages Required
1 page

```html
<!DOCTYPE html>
<html lang="en">
<head>
<meta charset="utf-8">
<title>Quarnela – Woodworks, Stoneworks &amp; Restoration</title>
<link href="https://fonts.googleapis.com/css2?family=Questrial&family=Lato:wght@400;700&family=Raleway:wght@600;700&display=swap" rel="stylesheet">
<style>
:root{
  --blue:#1b86d8;
  --blue-dark:#0f6fc0;
  --green:#5cbb3a;
  --ink:#222;
  --text:#333;
  --muted:#555;
  --band:#f5f5f5;
  --white:#fff;
  --rule:#d9d9d9;
  --dark:#1d1d1d;
  --darker:#0c0c0c;
  --footer-text:#e6e6e6;
}
*{margin:0;padding:0;box-sizing:border-box}
html,body{width:1200px;height:2795px;overflow:hidden}
body{position:relative;background:var(--white);font-family:"Lato",sans-serif;color:var(--text)}
.abs{position:absolute}
.heading{font-family:"Questrial",sans-serif}

/* header */
.site-header{left:0;top:0;width:1200px;height:129px;background:var(--white);box-shadow:0 2px 6px rgba(0,0,0,.15);z-index:2}
.brand{left:62px;top:38px;display:flex;align-items:center;gap:14px}
.brand-mark{width:40px;height:40px;background:var(--green)}
.brand-name{font-family:"Questrial",sans-serif;font-size:40px;color:#3a3a3a;line-height:1}
.socials{left:838px;top:20px;display:flex;gap:10px}
.socials span{width:28px;height:28px;border-radius:50%;background:var(--blue)}
.lang{left:1002px;top:17px;width:136px;height:34px;border:2px solid #555;display:flex;align-items:center;gap:10px;padding-left:10px;font-size:15px;color:#222}
.lang .flag{width:36px;height:22px;background:linear-gradient(#243b7a,#c0303a)}
.lang svg{margin-left:6px}
.main-nav{left:600px;top:78px;width:560px;height:51px}
.main-nav a{position:absolute;top:5px;font-size:15px;color:#333;text-decoration:none;letter-spacing:.5px}
.main-nav a.active{color:var(--blue)}
.main-nav .underline{position:absolute;left:14px;top:48px;width:58px;height:3px;background:var(--blue)}
.main-nav .sep{position:absolute;top:2px;width:1px;height:22px;background:var(--rule)}

/* hero */
.hero{left:0;top:129px;width:1200px;height:464px;background:linear-gradient(135deg,#4e433d 0%,#8d7a6c 40%,#5f5a58 70%,#3a3735 100%)}
.hero-shade{position:absolute;inset:0;background:rgba(20,20,20,.35)}
.hero-title{left:0;top:306px;width:1200px;text-align:center;font-family:"Questrial",sans-serif;font-size:38px;color:#fff}
.hero-text{left:300px;top:380px;width:600px;text-align:center;font-size:15px;line-height:21px;color:#f2f2f2}
.dots{left:578px;top:550px;display:flex;gap:5px}
.dots span{width:11px;height:11px;border-radius:50%;background:#fff}
.dots span.on{background:var(--blue)}

/* estimate */
.estimate{left:0;top:593px;width:1200px;height:134px;background:var(--white);border-bottom:3px solid #e2e2e2}
.estimate-text{left:62px;top:44px;font-family:"Questrial",sans-serif;font-size:35px;color:var(--ink)}
.btn-quote{left:935px;top:44px;width:203px;height:47px;border-radius:24px;background:var(--green);color:#fff;font-family:"Raleway",sans-serif;font-weight:700;font-size:19px;letter-spacing:1px;display:flex;align-items:center;justify-content:center}

/* services */
.band-grey{left:0;width:1200px;background:var(--band)}
.band-white{left:0;width:1200px;background:var(--white)}
.section-title{left:0;top:752px;width:1200px;text-align:center;font-family:"Questrial",sans-serif;font-size:35px;color:var(--ink)}
.section-title em{font-style:normal;color:var(--blue)}
.title-rule{left:572px;top:797px;width:56px;height:2px;background:var(--blue)}
.photo{border:2px solid #c8c8c8;overflow:hidden}
.photo .thumbs{position:absolute;bottom:10px;left:46px;display:flex;gap:4px}
.photo .thumbs span{width:88px;height:76px;border:2px solid #fff}
.photo .arrow{position:absolute;bottom:36px}
.svc-title{font-family:"Questrial",sans-serif;font-size:27px;color:var(--ink)}
.svc-text{font-size:14.5px;line-height:29.5px;color:var(--text)}
.btn-more{width:140px;height:38px;border-radius:19px;background:var(--blue);color:#fff;font-weight:700;font-size:14.5px;display:flex;align-items:center;justify-content:center;letter-spacing:.3px}
.tabs{left:0;width:1200px;display:flex;justify-content:center;gap:26px;font-family:"Questrial",sans-serif;font-size:17px;color:#333}
.tabs span.active{color:var(--blue);border-bottom:2px solid var(--blue);padding-bottom:2px}

/* about */
.about{left:0;top:2083px;width:1200px;height:350px;background:linear-gradient(120deg,#2b2b2b,#4a4540 50%,#2a2a2a)}
.about-shade{position:absolute;inset:0;background:rgba(10,10,10,.5)}
.about-title{left:529px;top:2127px;width:164px;text-align:center;font-family:"Questrial",sans-serif;font-size:35px;color:#fff}
.about-rule{left:508px;top:2170px;width:186px;height:1px;background:#ccc}
.about-brand{left:108px;top:2264px;display:flex;align-items:center;gap:16px}
.about-brand .brand-mark{width:48px;height:48px}
.about-brand .brand-name{font-size:46px;color:#fff}
.about-line{left:432px;top:2204px;width:2px;height:185px;background:var(--blue)}
.about-text{left:484px;top:2194px;width:656px;font-size:14.5px;line-height:29px;color:#f0f0f0}
.about-sign{left:484px;top:2344px;font-size:15.5px;line-height:25px;color:#fff}
.about-sign b{font-weight:700}

/* footer */
.site-footer{left:0;top:2433px;width:1200px;height:306px;background:linear-gradient(90deg,#050505,#1a1a1a 25%,#0a0a0a 50%,#1a1a1a 75%,#050505)}
.foot-title{top:2476px;font-family:"Raleway",sans-serif;font-weight:700;font-size:27px;color:#fff}
.foot-title em{font-style:normal;color:var(--blue)}
.quick-links{left:62px;top:2525px;list-style:none;font-size:13.5px;color:var(--footer-text)}
.quick-links li{height:32px;display:flex;align-items:center;gap:10px}
.quick-links li::before{content:"";border-left:5px solid #ccc;border-top:4px solid transparent;border-bottom:4px solid transparent}
.contact-row{left:320px;display:flex;align-items:flex-start;gap:16px;font-size:14.5px;color:var(--footer-text);line-height:20px}
.contact-row .ico{width:30px;height:30px;border:2px solid var(--blue);border-radius:50%;display:flex;align-items:center;justify-content:center;flex-shrink:0}
.field{left:639px;width:288px;border:1px solid #bbb;background:transparent;font-size:12px;color:#ddd;padding:8px 10px}
.btn-submit{left:635px;top:2681px;width:155px;height:41px;border:2px solid var(--blue);border-radius:20px;color:#fff;font-weight:700;font-size:15.5px;display:flex;align-items:center;justify-content:center;letter-spacing:.5px}
.follow{left:1008px;top:2525px;list-style:none;font-size:13.5px;color:var(--footer-text)}
.follow li{height:32px;display:flex;align-items:center;gap:12px}
.follow li span{width:20px;height:20px;background:#fff}
.copyright{left:0;top:2739px;width:1200px;height:56px;background:#000;color:#ddd;font-size:13px;display:flex;align-items:center;justify-content:center}
</style>
</head>
<body>

<header class="abs site-header">
  <div class="abs brand"><span class="brand-mark"></span><span class="brand-name">Quarnela</span></div>
  <div class="abs socials"><span></span><span></span><span></span><span></span></div>
  <div class="abs lang"><span class="flag" role="img" aria-label="UK flag"></span>English
    <svg width="12" height="8" viewBox="0 0 12 8"><path d="M0 0h12L6 8z" fill="#222"/></svg></div>
  <nav class="abs main-nav">
    <a class="active" style="left:22px">HOME</a>
    <span class="underline"></span>
    <span class="sep" style="left:115px"></span>
    <a style="left:145px">SERVICES</a>
    <span class="sep" style="left:259px"></span>
    <a style="left:293px">ABOUT US</a>
    <span class="sep" style="left:415px"></span>
    <a style="left:464px">CONTACT</a>
  </nav>
</header>

<section class="abs hero" role="img" aria-label="Carpenter measuring and cutting a timber board on a worksite">
  <div class="hero-shade"></div>
</section>
<h1 class="abs hero-title">Welcome to Quarnela</h1>
<p class="abs hero-text">At vero eos et accusamus et iusto odio dignissimos ducimus qui blanditiis praesentium voluptatum deleniti atque corrupti quos dolores et quas</p>
<div class="abs dots"><span class="on"></span><span></span><span></span></div>

<section class="abs estimate">
  <p class="abs estimate-text">Are you interested in an estimate?</p>
  <div class="abs btn-quote">GET A QUOTE</div>
</section>

<!-- services -->
<div class="abs band-grey" style="top:727px;height:497px"></div>
<div class="abs band-white" style="top:1224px;height:429px"></div>
<div class="abs band-grey" style="top:1653px;height:430px"></div>

<h2 class="abs section-title">Our <em>Services</em></h2>
<div class="abs title-rule"></div>

<!-- woodworks -->
<div class="abs photo" style="left:61px;top:857px;width:453px;height:298px;background:linear-gradient(135deg,#a8855e,#d8c29a 45%,#7e6a52)" role="img" aria-label="Builders in hard hats and safety vests working with timber">
  <div class="thumbs"><span style="background:#6b4a33"></span><span style="background:#b89a7c"></span><span style="background:#a46f42"></span><span style="background:#c7703a"></span></div>
  <svg class="arrow" style="right:8px" width="12" height="20" viewBox="0 0 12 20"><path d="M2 2l8 8-8 8" stroke="#333" stroke-width="2" fill="none"/></svg>
</div>
<h3 class="abs svc-title" style="left:546px;top:863px">Woodworks</h3>
<p class="abs svc-text" style="left:546px;top:906px;width:566px">&nbsp;Timber is, in essence, a natural and warm material. Wood is also relatively durable and easy to workwith, which has made it a favourite of builders throughout history. Our goal is to offer GALLERY (sliders) suitable products and quality furniture with installation and after - When cliked opens sales service to all of our clients. In order to achieve this, we're this category gallery ready to help our clients in all stages of construction from design to production and maintenance.</p>
<div class="abs btn-more" style="left:548px;top:1094px">READ MORE</div>
<div class="abs tabs" style="top:1177px"><span class="active">Furniture</span><span>Windows</span><span>Doors</span><span>Staircases</span><span>Woodcarving</span><span>Graining</span></div>

<!-- stoneworks -->
<h3 class="abs svc-title" style="left:62px;top:1297px">STONEWORKS</h3>
<p class="abs svc-text" style="left:62px;top:1340px;width:580px">The natural stone found in the ground has been used in construction for centuries because of its durability. A structure GALLERY (sliders) built by a skilled craftsman from natural stone is unique, genuine When cliked opens and durable, and perfect for our bracing climate. this category gallery Our experienced craftsmen are ready to help you in all stages of construction from planning to completion.</p>
<div class="abs btn-more" style="left:65px;top:1509px">READ MORE</div>
<div class="abs photo" style="left:684px;top:1273px;width:454px;height:298px;background:linear-gradient(135deg,#e8e2d6,#b8a68a 50%,#d9d2c4)" role="img" aria-label="Kitchen with stone countertops and cream cabinets">
  <div class="thumbs"><span style="background:#7f7a70"></span><span style="background:#8a5a3a"></span><span style="background:#6e7a68"></span><span style="background:#5a5550"></span></div>
  <svg class="arrow" style="left:10px" width="12" height="20" viewBox="0 0 12 20"><path d="M10 2L2 10l8 8" stroke="#333" stroke-width="2" fill="none"/></svg>
  <svg class="arrow" style="right:8px" width="12" height="20" viewBox="0 0 12 20"><path d="M2 2l8 8-8 8" stroke="#333" stroke-width="2" fill="none"/></svg>
</div>
<div class="abs tabs" style="top:1598px"><span class="active">Walls</span><span>Terraces</span><span>Paths</span><span>Outdoor kitchens</span><span>Fireplaces</span><span>Smokeries</span><span>Fences</span></div>

<!-- restoration -->
<div class="abs photo" style="left:61px;top:1699px;width:453px;height:300px;background:linear-gradient(180deg,#b9cbe0 0%,#c9c2b4 40%,#8f8576 100%)" role="img" aria-label="Historic building facade covered in restoration scaffolding">
  <div class="thumbs" style="left:46px"><span style="background:#a98a62"></span><span style="background:#c8c4bc"></span><span style="background:#7d6a58"></span><span style="background:#9a5a40"></span></div>
</div>
<h3 class="abs svc-title" style="left:546px;top:1707px">Restoration</h3>
<p class="abs svc-text" style="left:546px;top:1750px;width:566px">It's good to see that fixing old things has become popular again in recent years and people are trying to find ways to preserve GALLERY (sliders) valuable old windows and pieces of furniture before deciding to When cliked opens replace them. &nbsp;It is possible to give a new life to almost any wooden door, Window, piece of furniture or staircase. The extensive experience &nbsp;of our craftsmen will help you achieve the desired result.</p>
<div class="abs btn-more" style="left:548px;top:1938px">READ MORE</div>
<div class="abs tabs" style="top:2030px"><span class="active">Furniture</span><span>Windows</span><span>Doors</span><span>Staircases</span><span>Floors</span><span>Special Projects</span></div>

<!-- about -->
<section class="abs about" role="img" aria-label="Craftsman measuring wood with a spirit level, darkened background">
  <div class="about-shade"></div>
</section>
<h2 class="abs about-title">About Us</h2>
<div class="abs about-rule"></div>
<div class="abs about-brand"><span class="brand-mark"></span><span class="brand-name">Quarnela</span></div>
<div class="abs about-line"></div>
<p class="abs about-text">Quarnela is a company whose business operations include &nbsp;&nbsp;making wooden products, restoration and building structures from natural stone. All of our products are made by craftsmen and specialists who have extensive experience and knowledge in their fields.The products we offer are always handmade and we take the requests and ideas of the specific client into account We &nbsp;always strive to achieve the best possible quality.</p>
<p class="abs about-sign"><b>Quality matters,</b><br>&nbsp;Quarnela</p>

<!-- footer -->
<footer class="abs site-footer"></footer>
<h4 class="abs foot-title" style="left:62px">Quick <em>link</em></h4>
<ul class="abs quick-links"><li>Home</li><li>About Us</li><li>Services</li><li>Contact Us</li></ul>

<h4 class="abs foot-title" style="left:324px">Contact <em>Us</em></h4>
<div class="abs contact-row" style="top:2525px">
  <span class="ico"><svg width="12" height="16" viewBox="0 0 12 16"><path d="M6 0a6 6 0 0 1 6 6c0 4-6 10-6 10S0 10 0 6a6 6 0 0 1 6-6zm0 3.5a2.5 2.5 0 1 0 0 5 2.5 2.5 0 0 0 0-5z" fill="var(--blue)"/></svg></span>
  <div><b>Quarnela</b><br>Kalda 12 10115 Norvik<br>ESTLAND</div>
</div>
<div class="abs contact-row" style="top:2598px;align-items:center">
  <span class="ico"><svg width="14" height="14" viewBox="0 0 24 24"><path d="M6.6 10.8a15 15 0 0 0 6.6 6.6l2.2-2.2a1 1 0 0 1 1-.25 11.4 11.4 0 0 0 3.6.57 1 1 0 0 1 1 1V20a1 1 0 0 1-1 1A17 17 0 0 1 3 4a1 1 0 0 1 1-1h3.5a1 1 0 0 1 1 1c0 1.25.2 2.45.57 3.57a1 1 0 0 1-.25 1z" fill="#fff"/></svg></span>
  <span>555.018.2746</span>
</div>
<div class="abs contact-row" style="top:2648px;align-items:center">
  <span class="ico"><svg width="14" height="10" viewBox="0 0 14 10"><rect x=".5" y=".5" width="13" height="9" fill="none" stroke="#fff"/><path d="M.5.5L7 5.5 13.5.5" fill="none" stroke="#fff"/></svg></span>
  <span>sales@quarnela.com</span>
</div>

<h4 class="abs foot-title" style="left:643px">Quick <em>Inquiry</em></h4>
<div class="abs field" style="top:2528px;height:36px">Name</div>
<div class="abs field" style="top:2573px;height:36px">Phone</div>
<div class="abs field" style="top:2618px;height:52px">Message</div>
<div class="abs btn-submit">SUBMIT</div>

<h4 class="abs foot-title" style="left:1008px">Follow <em>Us</em></h4>
<ul class="abs follow"><li><span></span>Linkwall</li><li><span></span>Chirpline</li><li><span></span>Circleplus</li><li><span></span>Workmesh</li></ul>

<div class="abs copyright">Copyright © 2016 Quarnela. All Rights Reserved.</div>

</body>
</html>
```